Hollin Reach (we have a logo but are open to options ) (we hand make 100% soy candles & other hom

See our webpage for ideas www.hollinreach.com.
We need packaging for our Universal Jars in 5 different fragrances to start with & need to be able to add new lines along the way.
The box needs to be uniformed and then adding what is required to reflect each fragrance as we add them on the line. Eg. Midnight Orchard, Pear & Cedar, Nordic Heather, Sandal & Plum, Calm Peppermint (&; these could change).
There will also be matching boxes required for Reed Diffusers, Tealights and so on in our range.
-We want a white box, with a lux look, and kept simple. (We think an embossed logo might give it that lux look).
-We need to add things to our box like, warning instructions, burn instructions, barcodes etc.
-We are also changing our instragram account with our colour palette which will be backgrounds of white and pastel pinks, pink shades, some grey & black.
It's a chic lux sophicated look! Thank you.
16/06/18 We have just updated this brief. I have attached a colour palette picture. Ideally we would like the box to be white with embossed logo and maybe textured print on the sides or a chic print on the sides. The whole box appears to be too busy. It needs to look more feminine. On the colour palette, those colours could be used to write each different fragrance or the fragrance could be written in those colours. We hope this makes sense. We look forward to working with someone and hopefully we can use Skye or facetime to explain ourselves better. :)
Many Thanks, we hope you have fun with it.

Target Market(s)

People between ages of 18 to 50

Industry/Entity Type

Retail

Font styles to use
Sans Serif

Colors
ffffff
e667a6
eda3c7
f9d9e8
fdf0f6
959595
dbdbdb

Requirements
Must have
• Lux look with nice clean lines keeping it simple
• Obvioulsy, colours will change slightly when the box is introduced with a new fragrance to suit. Eg. Calm Peppermint (yellow /green)
Nice to have
• Pattern for the fragrance to differ the uniformity of the boxes to the brand.
• 100% Soy Wax.

```html
<!DOCTYPE html>
<html lang="en">
<head>
<meta charset="utf-8">
<title>Hollin Reach – Soy Wax Candle Boxes</title>
<link rel="stylesheet" href="https://fonts.googleapis.com/css2?family=Cormorant+Garamond:wght@500&display=swap">
<style>
  :root {
    --page: #ffffff;
    --box-face: #f3f2f0;
    --box-edge: #e8e6e3;
    --ink: #5a5a5a;
    --rule: #6a6a6a;
    --pear-accent: #f7babd;
    --pear-band: #f5b3b6;
    --pepper-accent: #1db47b;
    --pepper-band: #22b57e;
    --label-ink: #ffffff;
  }
  * { box-sizing: border-box; margin: 0; padding: 0; }
  html, body {
    width: 1200px;
    height: 795px;
    overflow: hidden;
    background: var(--page);
  }
  .canvas {
    position: relative;
    width: 1200px;
    height: 795px;
    font-family: "Cormorant Garamond", "Times New Roman", serif;
    font-variant-numeric: lining-nums;
    color: var(--ink);
  }
  .box {
    position: absolute;
    width: 422px;
    height: 509px;
    background: linear-gradient(90deg, var(--box-face) 0%, #f6f5f3 60%, var(--box-edge) 100%);
    box-shadow: 0 1px 2px rgba(0,0,0,0.08);
    overflow: hidden;
  }
  .box--pear { left: 130px; top: 129px; --accent: var(--pear-accent); --band: var(--pear-band); }
  .box--pepper { left: 651px; top: 131px; --accent: var(--pepper-accent); --band: var(--pepper-band); }

  .brand-tab {
    position: absolute;
    left: 0;
    top: 0;
    width: 79px;
    height: 146px;
    background: var(--accent);
    display: flex;
    flex-direction: column;
    justify-content: center;
    align-items: center;
    color: var(--label-ink);
    font-size: 17px;
    line-height: 1.15;
    text-align: center;
    letter-spacing: 0.02em;
  }
  .wax-claim {
    position: absolute;
    left: 29px;
    top: 246px;
    font-size: 24px;
    line-height: 26px;
    text-transform: uppercase;
  }
  .fragrance {
    position: absolute;
    left: 29px;
    top: 320px;
    font-size: 23px;
    line-height: 28px;
    font-weight: 500;
    text-transform: uppercase;
    letter-spacing: 0.01em;
    white-space: nowrap;
  }
  .rule {
    position: absolute;
    left: 29px;
    top: 380px;
    width: 43px;
    height: 2px;
    background: var(--rule);
  }
  .origin {
    position: absolute;
    left: 29px;
    top: 390px;
    font-size: 15px;
    line-height: 18px;
    letter-spacing: 0.1em;
    text-transform: uppercase;
    white-space: nowrap;
  }
  .pattern-band {
    position: absolute;
    left: 0;
    bottom: 0;
    width: 100%;
    height: 86px;
    background: var(--band);
  }
</style>
</head>
<body>
<main class="canvas">
  <section class="box box--pear">
    <div class="brand-tab"><span>Hollin</span><span>Reach</span></div>
    <p class="wax-claim">100%<br>Soy Wax</p>
    <h2 class="fragrance">Pear &amp; Cedar</h2>
    <div class="rule"></div>
    <p class="origin">Australian Made &amp; Hand Poured</p>
    <div class="pattern-band" role="img" aria-label="Tone-on-tone floral pattern in soft pink"></div>
  </section>

  <section class="box box--pepper">
    <div class="brand-tab"><span>Hollin</span><span>Reach</span></div>
    <p class="wax-claim">100%<br>Soy Wax</p>
    <h2 class="fragrance">Calm Peppermint</h2>
    <div class="rule"></div>
    <p class="origin">Australian Made &amp; Hand Poured</p>
    <div class="pattern-band" role="img" aria-label="Tone-on-tone floral pattern in fresh green"></div>
  </section>
</main>
</body>
</html>
```